Larkvale Metal Capability Statement

Email template to promote our companies capabilities

Target Market(s)

Building companies
Architects

Requirements
Must have
• product list
• Our Products Include
• Boxes
• Brackets
• Boardwalk Frames
• Cable Ladder & Tray
• Cabinets
• Custom Pressings
• Decorative Cladding
• Decorative Panels
• Flashings
• Gates
• Louvered Panels
• Metal Roof Battens
• Metal Scaffold Planks
• Metal Art
• Purlins
• Perforated Metals
• Room Dividers
• Scaffold Planks
• Steel Angles
• Street Furniture
• Shelving & Storage Systems
• Stair Treads
• Stud Framing
• Tanks
• Tool Boxes
• Waste Bins
• Services
• Guillotining
• CNC Bending
• Punching
• Stamping
• Notching
• Cropping
• Coil Blanking
• Turret Punching
• Drilling and tapping
• Welding (MIG & TIG)

```html
<!DOCTYPE html>
<html lang="en">
<head>
<meta charset="utf-8">
<title>Larkvale Metal – Capability</title>
<link href="https://fonts.googleapis.com/css2?family=Open+Sans:wght@400;600;700&display=swap" rel="stylesheet">
<style>
:root{
  --page:#f6f6f6;
  --white:#ffffff;
  --red:#d3302f;
  --red-dark:#a81f24;
  --ink:#333333;
  --body:#444444;
  --muted:#7a7a7a;
  --panel:#ebebeb;
  --rule:#dddddd;
  --footer:#333333;
  --footer-base:#262626;
  --footer-text:#f1f1f1;
  --social-a:#3b5998;
  --social-b:#1a87c9;
}
*{margin:0;padding:0;box-sizing:border-box}
html,body{width:682px;height:1200px;overflow:hidden;background:var(--page);font-family:"Open Sans",Arial,sans-serif;color:var(--body)}
.browser-link{height:41px;text-align:center;font-size:7px;color:var(--muted);padding-top:16px}
.browser-link span{text-decoration:underline}
.email{width:455px;margin-left:114px;background:var(--white)}
.header{height:58px;position:relative}
.brand{position:absolute;left:10px;top:21px;display:flex;align-items:center;gap:5px}
.brand-mark{width:14px;height:14px;border-radius:50%;background:var(--red)}
.brand-name{font-size:13px;font-weight:600;color:var(--red);line-height:14px}
.header-phone{position:absolute;right:13px;top:20px;font-size:11px;font-weight:700;color:var(--ink);display:flex;align-items:center;gap:4px}
.hero{height:179px;position:relative;background:linear-gradient(180deg,#9fb3c6 0%,#c8d2da 35%,#b5b3ad 60%,#9c8672 100%)}
.hero-band{position:absolute;left:0;right:0;bottom:0;height:39px;background:rgba(211,48,47,.92);color:var(--white);font-size:16px;font-weight:700;padding:8px 13px}
.intro{height:178px;padding:21px 14px 0;font-size:9px;line-height:15px}
.intro p{margin-bottom:2px}
.intro strong{color:var(--ink);font-weight:700}
.products{height:309px;background:var(--panel);position:relative}
.section-title{font-size:14.5px;font-weight:700;color:var(--ink);position:absolute;left:14px}
.products .section-title{top:16px}
.list{position:absolute;list-style:none;font-size:8.5px;line-height:18.2px;color:var(--body)}
.list li{padding-left:13px;position:relative}
.list li::before{content:"";position:absolute;left:1px;top:6px;border-left:5px solid var(--red);border-top:3px solid transparent;border-bottom:3px solid transparent}
.products .list{top:42px}
.col-a{left:14px}
.products .col-b{left:153px}
.photo{position:absolute;border:2px solid var(--white)}
.ph-frame{left:268px;top:51px;width:168px;height:79px;background:linear-gradient(180deg,#a6b8c8,#b9b9b6 55%,#9a7c64)}
.ph-angles{left:268px;top:137px;width:168px;height:45px;background:linear-gradient(90deg,#c7ccd2,#e3e5e8,#a9afb6,#dfe2e5)}
.ph-seats{left:268px;top:189px;width:86px;height:45px;background:linear-gradient(90deg,#3a7fc4,#d27b3a 45%,#7fae5a)}
.ph-channel{left:361px;top:189px;width:75px;height:45px;background:linear-gradient(180deg,#8e9094,#d4d6d8 60%,#b39a6e)}
.ph-perforated{left:268px;top:241px;width:168px;height:45px;background:linear-gradient(90deg,#5c5c5c,#cfcfcf 30%,#3a3a3a 60%,#9a9a9a)}
.services{height:148px;position:relative;border-bottom:1px solid var(--rule)}
.services .section-title{top:13px}
.services .list{top:39px;font-size:9px}
.services .col-b{left:115px}
.ph-machine{position:absolute;left:268px;top:39px;width:168px;height:80px;background:linear-gradient(180deg,#3d3d40 0%,#2a2a2c 40%,#d9412c 60%,#b8b8b8 100%)}
.cta{height:69px;display:flex;justify-content:center;align-items:center;border-bottom:1px solid var(--rule)}
.cta-button{width:130px;height:33px;border-radius:17px;background:linear-gradient(180deg,var(--red),var(--red-dark));color:var(--white);font-size:13px;font-weight:700;display:flex;align-items:center;justify-content:center}
.badges{height:81px;position:relative}
.badge{position:absolute}
.badge-round{left:48px;top:12px;width:60px;height:54px;border-radius:50%;background:#e8ecf4;border:2px solid #1f3a8a}
.badge-quality{left:130px;top:23px;width:134px;height:36px;border:1.5px solid var(--red);background:var(--white)}
.badge-safety{left:278px;top:22px;width:139px;height:37px;border:1.5px solid #2c4fa3;background:var(--white)}
.badge-quality::before,.badge-safety::before{content:"";position:absolute;left:3px;top:3px;width:27px;height:27px;border-radius:50%}
.badge-quality::before{background:var(--red)}
.badge-safety::before{background:#2c4fa3}
.footer{height:95px;background:var(--footer);position:relative;color:var(--footer-text);font-size:8px}
.contact{position:absolute;top:14px;line-height:18.2px}
.contact b{font-weight:700}
.c1{left:19px}
.c2{left:98px}
.c3{left:240px}
.social{position:absolute;top:67px;width:17px;height:17px;border-radius:50%}
.s1{left:399px;background:var(--social-a)}
.s2{left:423px;background:var(--social-b)}
.copyright{height:30px;background:var(--footer-base);color:var(--footer-text);font-size:7px;text-align:center;line-height:30px}
</style>
</head>
<body>
<div class="browser-link">view it in <span>browser</span></div>
<main class="email">
  <header class="header">
    <div class="brand"><div class="brand-mark"></div><div class="brand-name">Larkvale Metal</div></div>
    <div class="header-phone">
      <svg width="12" height="12" viewBox="0 0 24 24"><path fill="#d3302f" d="M6.6 10.8a15.1 15.1 0 0 0 6.6 6.6l2.2-2.2c.3-.3.7-.4 1-.2 1.1.4 2.3.6 3.6.6.6 0 1 .4 1 1V20c0 .6-.4 1-1 1A17 17 0 0 1 3 4c0-.6.4-1 1-1h3.5c.6 0 1 .4 1 1 0 1.3.2 2.5.6 3.6.1.3 0 .7-.2 1z"/><path fill="none" stroke="#d3302f" stroke-width="2" d="M14 3a7 7 0 0 1 7 7M14 7a3 3 0 0 1 3 3"/></svg>
      (08) 5550 1420
    </div>
  </header>
  <section class="hero" role="img" aria-label="Photo of a steel roof and wall frame under construction on a building site">
    <div class="hero-band">Capability</div>
  </section>
  <section class="intro">
    <p><strong>Larkvale Metal Form.... Steel Done Right!</strong><br>Established in 1981, we manufacture quality steel components to the building, mining and electrical industries. Offering friendly and personalised service for all your steel needs, we can customise our products dependant on our customer needs.</p>
    <p>We have manufacturing locations in Perth, Sydney, Brisbane and Townsville.</p>
    <p>We pride ourselves on fast turn around to meet our customer’s time frames and flexibility whilst maintaining our excellent value for money and producing high quality products.</p>
    <p>Our experienced fabricators use only the latest in CNC equipment to produce only the highest of quality products and services from larger steel jobs right through to simple spot welding.</p>
  </section>
  <section class="products">
    <h2 class="section-title">Our Products</h2>
    <ul class="list col-a">
      <li>Boxes</li><li>Brackets</li><li>Boardwalk Frames</li><li>Cable Ladder &amp; Tray</li><li>Cabinets</li><li>Custom Pressings</li><li>Decorative Cladding</li><li>Decorative Panels</li><li>Flashings</li><li>Gates</li><li>Street Furniture</li><li>Shelving &amp; Storage Systems</li><li>Stair Treads</li>
    </ul>
    <ul class="list col-b">
      <li>Louvered Panels</li><li>Metal Roof Battens</li><li>Metal Scaffold Planks</li><li>Metal Art</li><li>Purlins</li><li>Perforated Metals</li><li>Room Dividers</li><li>Scaffold Planks</li><li>Steel Angles</li><li>Stud Framing</li><li>Tanks</li><li>Tool Boxes</li><li>Waste Bins</li>
    </ul>
    <div class="photo ph-frame" role="img" aria-label="Photo of a steel house frame on site"></div>
    <div class="photo ph-angles" role="img" aria-label="Photo of stacked steel angles"></div>
    <div class="photo ph-seats" role="img" aria-label="Photo of coloured metal street seating"></div>
    <div class="photo ph-channel" role="img" aria-label="Photo of stacked steel channel sections"></div>
    <div class="photo ph-perforated" role="img" aria-label="Photo of perforated metal sheets and decorative metal art"></div>
  </section>
  <section class="services">
    <h2 class="section-title">Services</h2>
    <ul class="list col-a">
      <li>Guillotining</li><li>CNC Bending</li><li>Punching</li><li>Stamping</li><li>Notching</li>
    </ul>
    <ul class="list col-b">
      <li>Cropping</li><li>Coil Blanking</li><li>Turret Punching</li><li>Drilling and tapping</li><li>Welding (MIG &amp; TIG)</li>
    </ul>
    <div class="ph-machine" role="img" aria-label="Photo of a CNC turret punch press in the workshop"></div>
  </section>
  <section class="cta"><div class="cta-button">Quote Now!</div></section>
  <section class="badges">
    <div class="badge badge-round"></div>
    <div class="badge badge-quality"></div>
    <div class="badge badge-safety"></div>
  </section>
  <footer class="footer">
    <div class="contact c1"><b>Contacts</b><br>Head Office<br>08 5550 1420</div>
    <div class="contact c2"><b>Dana Whitcombe</b><br>State Manager<br>08 5550 3106<br>d.whitcombe@larkvalemetal.com.au</div>
    <div class="contact c3"><b>Glen Harrow</b><br>Sales Manager<br>08 5550 3139<br>glen.harrow@larkvalemetal.com.au</div>
    <div class="social s1"></div>
    <div class="social s2"></div>
  </footer>
  <div class="copyright">© 2019 Larkvale Metal Form. All Rights Reserved</div>
</main>
</body>
</html>
```